Letter head / email signature/ contract document templates

We need a professional email signature and letterhead designed for our established carpentry and maintenance company. Our Logo (attached) was originally designed 6 years ago by design guru and we love it, looking for something to compliment it ( not a home job)

```html
<!DOCTYPE html>
<html lang="en">
<head>
<meta charset="utf-8">
<title>Kestrel Repairs – Email Signature &amp; Letterhead</title>
<link href="https://fonts.googleapis.com/css2?family=Questrial&display=swap" rel="stylesheet">
<style>
  :root{
    --backdrop:#2a2a2a;
    --paper:#ffffff;
    --brand-red:#d42027;
    --ink-dark:#3f3f41;
    --ink-body:#4a4a4a;
    --divider:#e8735a;
    --tint:#f2f2f3;
  }
  *{box-sizing:border-box;margin:0;padding:0}
  html,body{width:830px;height:1200px;overflow:hidden}
  body{background:var(--backdrop);font-family:"Questrial",sans-serif;position:relative}

  .email-signature{position:absolute;left:111px;top:74px;width:609px;height:154px;background:var(--paper);overflow:hidden}
  .letterhead{position:absolute;left:110px;top:270px;width:611px;height:857px;background:var(--paper);overflow:hidden}

  .brand{position:absolute;display:flex;align-items:center;gap:6px;color:var(--ink-dark);font-size:16px;line-height:20px;white-space:nowrap;letter-spacing:.2px}
  .brand-mark{width:10px;height:10px;background:var(--brand-red);flex:none}
  .email-signature .brand{left:76px;top:64px}
  .letterhead .brand{left:21px;top:38px}

  .sig-divider{position:absolute;left:223px;top:34px;width:1px;height:83px;background:var(--divider)}
  .sig-details{position:absolute;left:233px;top:38px}
  .sig-name{color:var(--brand-red);font-size:15px;line-height:18px;text-transform:uppercase}
  .sig-role{color:var(--ink-body);font-size:8px;line-height:11px;margin-bottom:5px}

  .contact-list{list-style:none}
  .contact-list li{display:flex;align-items:center;gap:5px;white-space:nowrap}
  .sig-details .contact-list li{font-size:11.5px;line-height:15px;color:var(--ink-body)}
  .contact-icon{width:9px;height:9px;flex:none}

  .footer-band{position:absolute;left:0;bottom:0;width:611px;height:67px}
  .footer-contacts{position:absolute;left:437px;top:797px}
  .footer-contacts li{font-size:10.5px;line-height:13.5px;color:#fff}
</style>
</head>
<body>

<svg width="0" height="0" style="position:absolute" aria-hidden="true">
  <defs>
    <symbol id="icon-phone" viewBox="0 0 10 10"><circle cx="5" cy="5" r="5" fill="currentColor"/><path d="M3.2 2.6l1 .9-.5.8c.4.7.9 1.2 1.6 1.6l.8-.5.9 1-.6.8C5 7.1 2.9 5 2.8 3.2z" fill="var(--bg,#fff)"/></symbol>
    <symbol id="icon-mail" viewBox="0 0 10 10"><circle cx="5" cy="5" r="5" fill="currentColor"/><rect x="2.6" y="3.3" width="4.8" height="3.4" fill="var(--bg,#fff)"/><path d="M2.6 3.3L5 5.2l2.4-1.9" stroke="currentColor" stroke-width=".6" fill="none"/></symbol>
    <symbol id="icon-home" viewBox="0 0 10 10"><circle cx="5" cy="5" r="5" fill="currentColor"/><path d="M5 2.4l2.4 2.2v2.9H5.8V6H4.2v1.5H2.6V4.6z" fill="var(--bg,#fff)"/></symbol>
  </defs>
</svg>

<section class="email-signature" aria-label="Email signature">
  <div class="brand"><span class="brand-mark"></span>Kestrel Repairs</div>
  <div class="sig-divider"></div>
  <div class="sig-details">
    <p class="sig-name">Sam Carver</p>
    <p class="sig-role">Manager</p>
    <ul class="contact-list">
      <li><svg class="contact-icon" style="color:var(--brand-red)"><use href="#icon-phone"/></svg>111-222-333</li>
      <li><svg class="contact-icon" style="color:var(--brand-red)"><use href="#icon-mail"/></svg>info@kestrelrepairs.com</li>
      <li><svg class="contact-icon" style="color:var(--brand-red)"><use href="#icon-home"/></svg>Your address, your city, box 88900</li>
    </ul>
  </div>
</section>

<section class="letterhead" aria-label="Letterhead">
  <div class="brand"><span class="brand-mark"></span>Kestrel Repairs</div>
  <svg class="footer-band" viewBox="0 0 611 67" preserveAspectRatio="none" aria-hidden="true">
    <polygon points="165,0 611,0 611,67 228,67" fill="var(--brand-red)"/>
  </svg>
  <ul class="contact-list footer-contacts">
    <li><svg class="contact-icon" style="color:#fff;--bg:var(--brand-red)"><use href="#icon-phone"/></svg>111-222-333</li>
    <li><svg class="contact-icon" style="color:#fff;--bg:var(--brand-red)"><use href="#icon-mail"/></svg>info@kestrelrepairs.com</li>
    <li><svg class="contact-icon" style="color:#fff;--bg:var(--brand-red)"><use href="#icon-home"/></svg>Your address, your city, box 88900</li>
  </ul>
</section>

</body>
</html>
```